Label for a new chocolate snack

Hello. We are Meadow Sweets Store. We are a new company making healthy chocolate snacks. We need Labels for our first product: Orla's Chocolate Figs,

We have two varieties:

1) dark chocolate

2) milk chocolate

The labels are 4 inches wide by 6 inches height. They are being printed on white glossy paper. They will be going on Kraft bags.

Here is the info we need on the labels:

Orla's
Chocolate Dates
Peanut Butter Center
Milk Chocolate
8g of Protein
Great Source of Energy
175g.

Orlas Chocolate Figs are targeted towards women who are 20-45 years of age.
Our goal is to create products that are healthy and taste good at the same time.

Finally, we will be adding more variations in the future, such as almond butter center, so being able to change the theme of the label to match the center filling would be good.

Thank you to everyone who will be submitting a design and good luck.

Target Market(s)

Woman, 20-40 years old, shop at gourmet grocery stores and health food stores

Industry/Entity Type

It Company

Colors

Designer to choose colors to be used in the design.

Requirements
Must have
• Orla's
• Chocolate Dates
• Peanut Butter Centre
• Milk Chocolate / Dark Chocolate
• 8g of Protein
• Great Source of Energy
• 175g.
• Back side of label must have everything contained in the pdfs i have attached.
• We are looking for a upscale chocolate look. That will still stand out on the shelf.
Should not have
• Main colors should not be brown, or black.

```html
<!DOCTYPE html>
<html lang="en">
<head>
<meta charset="utf-8">
<title>Orla's Chocolate Figs – Milk Chocolate Label</title>
<link rel="stylesheet" href="https://fonts.googleapis.com/css2?family=Bebas+Neue&family=Dancing+Script:wght@500;600&family=Oswald:wght@500&display=swap">
<style>
  :root {
    --canvas: #f4f2ef;
    --label: #ffffff;
    --blush: #fae3ef;
    --ornament: #fbe9f2;
    --rose: #f27fbd;
    --cocoa: #3a2418;
    --cream: #ffffff;
    --choc-dark: #2b1a14;
    --choc-mid: #6b3a22;
    --choc-light: #b7784d;
  }
  * { margin: 0; padding: 0; box-sizing: border-box; }
  html, body { width: 1200px; height: 1200px; overflow: hidden; }
  body { background: var(--canvas); position: relative; }

  .label {
    position: absolute; left: 250px; top: 75px;
    width: 700px; height: 1050px;
    background: var(--label);
    overflow: hidden;
    box-shadow: 0 4px 18px rgba(0,0,0,0.12);
  }
  .label__shapes { position: absolute; inset: 0; }

  .ornament {
    position: absolute; left: 0; top: 0; width: 310px; height: 1050px;
    background: linear-gradient(90deg, var(--ornament) 0%, rgba(251,233,242,0.55) 70%, rgba(255,255,255,0) 100%);
  }

  .brand {
    position: absolute; left: 0; right: 0; top: 50px;
    text-align: center; color: var(--cocoa);
  }
  .brand__name {
    font-family: "Dancing Script", cursive; font-weight: 600;
    font-size: 96px; line-height: 1; letter-spacing: 1px;
    padding-left: 10px;
  }
  .brand__product {
    font-family: "Oswald", sans-serif; font-weight: 500;
    font-size: 27px; letter-spacing: 0.5px; margin-top: 4px;
  }
  .brand__filling {
    font-family: "Dancing Script", cursive; font-weight: 500;
    font-size: 23px; margin-top: 0;
  }

  .variety {
    position: absolute; left: 200px; width: 300px; top: 325px;
    text-align: center; color: var(--rose);
    font-family: "Bebas Neue", sans-serif;
  }
  .variety__main { font-size: 196px; line-height: 0.82; letter-spacing: 2px; }
  .variety__sub { font-size: 78px; line-height: 1; letter-spacing: 1px; margin-top: 14px; }

  .product-photo {
    position: absolute; left: 22px; top: 632px; width: 660px; height: 370px;
    border-radius: 140px 160px 120px 90px;
    background:
      radial-gradient(ellipse 16% 14% at 30% 52%, #e8a43d 0%, rgba(232,164,61,0) 100%),
      radial-gradient(ellipse 40% 55% at 30% 55%, var(--choc-dark) 0%, var(--choc-dark) 60%, rgba(43,26,20,0) 100%),
      linear-gradient(100deg, var(--choc-mid) 0%, var(--choc-dark) 35%, var(--choc-mid) 60%, var(--choc-light) 85%, #d7a07a 100%);
  }

  .claims {
    position: absolute; left: 200px; width: 300px; top: 870px;
    text-align: center; color: var(--cream);
    font-family: "Dancing Script", cursive; font-weight: 500;
    font-size: 25px; line-height: 1.3;
  }
</style>
</head>
<body>
  <main class="label">
    <svg class="label__shapes" width="700" height="1050" viewBox="0 0 700 1050" aria-hidden="true">
      <ellipse class="blush-arc blush-arc--top" cx="560" cy="55" rx="330" ry="225" fill="var(--blush)"/>
      <ellipse class="blush-arc blush-arc--bottom" cx="600" cy="880" rx="360" ry="290" fill="var(--blush)"/>
    </svg>

    <div class="ornament" role="img" aria-label="Soft pink line-drawn flower and leaf pattern along the left edge"></div>

    <header class="brand">
      <h1 class="brand__name">Orla's</h1>
      <p class="brand__product">CHOCOLATE DATES</p>
      <p class="brand__filling">peanut butter center</p>
    </header>

    <h2 class="variety">
      <span class="variety__main">MILK</span><br>
      <span class="variety__sub">CHOCOLATE</span>
    </h2>

    <div class="product-photo" role="img" aria-label="Photo of a milk chocolate coated date cut open to show its peanut butter center, beside a whole one"></div>

    <p class="claims">8g of Protein<br>Great Source of Energy<br>175g.</p>
  </main>
</body>
</html>
```